independent cleaner, reliable, custom, thorough, trustworthy

Not sure yet if I want single-sided or double sided, so I'm selecting double-sided just in case, but single-sided designs are okay.

Really looking to find the happy medium between personal and professional in a business card design. I end up building comfortable relationships with the people I work for.

Most of my business is through referrals, but I want some business cards to hand out to people who ask for one (and maybe put them on community bulletin boards).

My target market is homeowners and business owners who are looking for a reliable cleaner and are willing to pay a bit more to have excellent quality and someone they trust.

Theme: I have a personal-professional feel since I'm solo, so the theme should reflect that. Trustworthy, personal, simple. I clean up messes.

Hopefully this is enough info, let me know if you have any questions though of course!

Target Market(s)

Homeowners businessowners who are looking for a reliable cleaner, excellent quality trustworthy.

Industry/Entity Type

Cleaning Service

Contact Information for Business Card

Please include this text:
• Delphine Marrow
• independent cleaner
• reliable, custom, thorough
• 604-317-2296
• tbw.marrow@quillpost.net

Font styles to use
Serif
Sans Serif

Colors
ffffff
00a990
0492cd
33a6d7
0355a3
3276b5
919191

Requirements
Must have
• Really looking to find the happy medium between personal and professional in a business card design.
• Background: at least 50% white on the side with the most text (coloured accents or shapes are okay)
• I lean more towards simple and clean, solid colours, maybe a gentle gradient
Nice to have
• Not sure yet if I want single-sided or double sided, so I'm selecting double-sided just in case, but single-sided designs are okay.
• Colours: preferably blues and teals for the font and other objects (if any). Open to designer's choice though. I've toyed around with orangey-yellow, but it doesn't feel right and I keep going back to blues/teals
• Also I uploaded a sketch of my signature and initials so you can get a feel for my personality. I'm not expecting this to be included in the design, it's just there.
Should not have
• I don't like a lot of busy-ness or textures
• Also I don't have a logo (not sure where else to specify this)

```html
<!DOCTYPE html>
<html lang="en">
<head>
<meta charset="utf-8">
<title>Delphine Marrow – Independent Cleaner Business Card</title>
<link href="https://fonts.googleapis.com/css2?family=Lato:wght@400;700&display=swap" rel="stylesheet">
<style>
  :root {
    --white: #ffffff;
    --teal: #00a990;
    --blue: #0492cd;
    --blue-light: #33a6d7;
    --grey: #919191;
    --ink: #2b2b2b;
    --backdrop: #e9ecef;
  }
  * { margin: 0; padding: 0; box-sizing: border-box; }
  html, body {
    width: 1200px;
    height: 900px;
    overflow: hidden;
    background: var(--backdrop);
    font-family: "Lato", sans-serif;
  }
  .business-card {
    position: absolute;
    left: 150px;
    top: 171px;
    width: 900px;
    height: 557px;
    background: var(--white);
    overflow: hidden;
    box-shadow: 0 12px 36px rgba(0, 0, 0, 0.18);
  }
  .card-shapes {
    position: absolute;
    inset: 0;
  }
  .contact-list {
    position: absolute;
    left: 38px;
    top: 222px;
    list-style: none;
    color: var(--white);
    font-size: 28px;
    line-height: 1;
  }
  .contact-item {
    display: flex;
    align-items: center;
    gap: 8px;
    height: 54px;
    white-space: nowrap;
  }
  .contact-icon {
    width: 24px;
    height: 24px;
    flex: none;
  }
  .identity {
    position: absolute;
    left: 530px;
    top: 215px;
    width: 340px;
    text-align: center;
  }
  .identity-mark {
    display: block;
    width: 130px;
    height: 130px;
    margin: 0 auto 40px;
    border-radius: 50%;
    background: var(--blue);
  }
  .identity-name {
    color: var(--teal);
    font-size: 40px;
    font-weight: 400;
    line-height: 1;
    white-space: nowrap;
  }
  .identity-role {
    display: flex;
    align-items: center;
    gap: 10px;
    margin-top: 10px;
    color: var(--grey);
    font-size: 16px;
    letter-spacing: 0.5px;
    text-transform: uppercase;
  }
  .identity-role::before,
  .identity-role::after {
    content: "";
    flex: 1;
    height: 2px;
    background: var(--grey);
  }
  .tagline {
    margin-top: 14px;
    color: var(--ink);
    font-size: 26px;
    white-space: nowrap;
  }
</style>
</head>
<body>
  <article class="business-card">
    <svg class="card-shapes" width="900" height="557" viewBox="0 0 900 557" aria-hidden="true">
      <polygon class="accent-chevron" points="345,0 362,0 507,279 362,557 345,557" fill="#00a990"/>
      <polygon class="contact-panel" points="0,0 345,0 490,279 345,557 0,557" fill="#0492cd"/>
    </svg>

    <ul class="contact-list">
      <li class="contact-item">
        <svg class="contact-icon" viewBox="0 0 24 24" aria-hidden="true">
          <path fill="#ffffff" d="M3 8c0-2 4-4 9-4s9 2 9 4v2h-5V8c-1-.6-2.4-1-4-1s-3 .4-4 1v2H3z"/>
          <path fill="#ffffff" d="M7 11h10l3 8H4z"/>
          <circle cx="12" cy="15" r="2" fill="#0492cd"/>
        </svg>
        <span>604-317-2296</span>
      </li>
      <li class="contact-item">
        <svg class="contact-icon" viewBox="0 0 24 24" aria-hidden="true">
          <rect x="2" y="5" width="20" height="14" fill="#ffffff"/>
          <path d="M2.5 5.5 12 13l9.5-7.5" fill="none" stroke="#0492cd" stroke-width="1.6"/>
        </svg>
        <span>tbw.marrow@quillpost.net</span>
      </li>
    </ul>

    <section class="identity">
      <span class="identity-mark" aria-hidden="true"></span>
      <h1 class="identity-name">Delphine Marrow</h1>
      <p class="identity-role">Independent Cleaner</p>
      <p class="tagline">Reliable | Custom | Thorough</p>
    </section>
  </article>
</body>
</html>
```